Dwellings and Champions Website Re-design

Already Wordpress base. Needs to be updated and better presentation. Current site: www.valorbrook.example redirected from www.dwellingsandchamps.example
Site purpose is to offer information and get leads from potential heroes looking to buy, rent or sell a home
Here is a link to the video to be used as well: https://www.clipvault.example/watch?v=Zr8pLmT4wKa

I own the video and logo
The video spells out the program. We will need a page for REALTORS to sign up, a page for our Vendors and their benefits
Steadfast Lending, Marta Delvin offers a reduced rate plus they will pay the upfront cost of the $600 VA appraisal
Hero Buyers get 25% rebate after escrow
Hero Sellers get 25% off a normal 6% Listing
Pinecrest Inspections will give a 10% off discount for heroes
Also need a page for the Medic Pledge program

Direct competitor: www.housesforvalor.example

Target Market(s)

veterans, teachers, government employees, nurses, 1st responders

Industry/Entity Type

Realtor

Coding

Coded - Design and coding required

Number of Pages Required

5+ page

Font styles to use

Colors
ec1f27
ffffff
3176b5

Requirements
Must have
• clean and correct throughout, ability to collect leads with FB login, or names and phone and email information. Colors are Navy Blue, Burgandy Red, and White
Nice to have
• photos

```html
<!DOCTYPE html>
<html lang="en">
<head>
<meta charset="utf-8">
<title>Dwellings and Champions</title>
<link rel="stylesheet" href="https://fonts.googleapis.com/css2?family=Raleway:ital,wght@0,400;0,500;0,600;0,700;1,400&display=swap">
<style>
:root{
  --navy:#0e1f5b;
  --navy-deep:#0a1030;
  --burgundy:#8c1119;
  --burgundy-dark:#7a0f16;
  --red:#ec1f27;
  --white:#ffffff;
  --gray-bg:#f3f3f3;
  --text:#333333;
  --muted:#666666;
  --footer:#0b1127;
  --footer-bar:#05070f;
}
*{box-sizing:border-box;margin:0;padding:0}
html,body{width:1200px;height:2932px;overflow:hidden}
body{font-family:"Raleway",sans-serif;color:var(--text);background:var(--white);position:relative}
section,header,footer{position:relative;width:1200px}

/* hero */
.hero{height:578px;background:linear-gradient(160deg,#7b3a17 0%,#b4631f 30%,#d69a4a 48%,#8a4b1c 70%,#3e2410 100%)}
.hero-photo{position:absolute;inset:0}
.topbar{position:absolute;left:0;top:0;width:1200px;height:125px;background:rgba(255,255,255,.82)}
.brand{position:absolute;left:84px;top:34px;font-size:30px;font-weight:700;color:var(--navy);line-height:34px;width:200px}
.account{position:absolute;left:790px;top:44px;font-size:13px;font-weight:600;color:var(--navy-deep);display:flex;align-items:center;gap:8px}
.social{position:absolute;left:972px;top:42px;display:flex;gap:14px}
.social span{width:20px;height:20px;border-radius:50%;background:var(--burgundy);display:block}
.nav{position:absolute;left:298px;top:92px;display:flex;gap:36px;font-size:13px;font-weight:600;color:var(--navy-deep)}
.hero-title{position:absolute;top:262px;width:100%;text-align:center;color:var(--white);font-size:50px;font-weight:700;font-variant:small-caps;letter-spacing:1px}
.hero-sub{position:absolute;top:332px;width:100%;text-align:center;color:var(--white);font-size:30px;font-weight:400;font-variant:small-caps;letter-spacing:1px}
.search-tabs{position:absolute;left:86px;top:512px;display:flex}
.search-tabs span{height:25px;padding:0 20px;font-size:13px;font-weight:600;color:var(--white);line-height:25px}
.tab-buyer{background:var(--navy)}
.tab-seller{background:var(--burgundy)}
.search-panel{position:absolute;left:86px;top:537px;width:1028px;height:82px;background:var(--navy);display:flex;align-items:center;padding-left:32px;gap:24px}
.select{width:222px;height:36px;background:var(--white);font-size:11px;color:#888;display:flex;align-items:center;justify-content:space-between;padding:0 14px}
.select::after{content:"";border:6px solid transparent;border-top:7px solid #222;margin-top:6px}
.btn-submit{width:222px;height:36px;background:var(--burgundy);color:var(--white);font-size:15px;font-weight:600;text-align:center;line-height:36px}

/* savings */
.savings{height:559px;margin-top:82px;background:var(--gray-bg)}
.savings-head{position:absolute;top:58px;width:100%;text-align:center;font-size:33px;font-weight:400;color:#333;letter-spacing:1px}
.savings-amount{position:absolute;top:104px;width:100%;text-align:center;font-size:33px;font-weight:500;color:#111}
.savings-amount::before,.savings-amount::after{content:"";position:absolute;top:24px;width:90px;height:1px;background:#ccc}
.savings-amount::before{left:378px}.savings-amount::after{right:378px}
.hero-grid{position:absolute;left:86px;top:228px;width:1028px;display:grid;grid-template-columns:repeat(3,1fr);row-gap:70px}
.hero-grid::after{content:"";position:absolute;left:0;right:0;top:128px;height:1px;background:#dcdcdc}
.hero-type{display:flex;gap:20px}
.hero-type .icon{width:92px;height:92px;border-radius:50%;background:var(--navy);flex:none}
.hero-type h3{font-size:16px;font-weight:500;color:#222;margin-top:8px}
.hero-type h3::after{content:"";display:block;width:36px;height:1px;background:#999;margin:8px 0 10px}
.hero-type p{font-size:10.5px;line-height:16px;color:#555;width:226px}
.hero-type a{font-size:10.5px;color:var(--burgundy);text-decoration:none}

/* how it works */
.how{height:444px}
.video{position:absolute;left:86px;top:47px;width:500px;height:338px;background:linear-gradient(135deg,#1e4f93,#2a65b0 60%,#1c4680)}
.how h2{position:absolute;left:635px;top:74px;font-size:37px;font-weight:400;color:#222}
.how h2::after{content:"";position:absolute;left:318px;top:24px;width:80px;height:1px;background:#ccc}
.how-body{position:absolute;left:635px;top:134px;width:490px}
.how-text{font-size:12.5px;line-height:21px;color:#666}
.how-text p+p{margin-top:20px}
.btn-more{margin-top:26px;width:138px;height:44px;background:var(--burgundy);color:var(--white);font-size:13px;text-align:center;line-height:44px;margin-left:2px}

/* advantages */
.advantages{height:473px;background:var(--burgundy)}
.section-title{position:absolute;width:100%;text-align:center;font-size:36px;font-weight:400}
.section-title::before,.section-title::after{content:"";position:absolute;top:22px;width:70px;height:1px}
.advantages .section-title{top:55px;color:var(--white)}
.advantages .section-title::before,.advantages .section-title::after{background:rgba(255,255,255,.7)}
.advantages .section-title::before{left:334px}.advantages .section-title::after{right:334px}
.adv-grid{position:absolute;left:86px;top:152px;display:flex;gap:28px}
.adv{width:324px;text-align:center;color:var(--white)}
.adv .photo{height:157px}
.photo-officers{background:linear-gradient(135deg,#3a3a3a,#8a7a6a 55%,#1a1a22)}
.photo-family{background:linear-gradient(135deg,#7a3d1a,#d08a3a 55%,#4a2a14)}
.photo-medics{background:linear-gradient(135deg,#3f6b8c,#c8b0a0 55%,#8a2a20)}
.adv h3{font-size:24px;font-weight:700;margin-top:22px}
.adv p{font-size:13px;line-height:24px;margin-top:10px;padding:0 24px}

/* reviews */
.reviews{height:410px}
.reviews .section-title{top:68px;color:#222}
.reviews .section-title::before,.reviews .section-title::after{background:#ccc}
.reviews .section-title::before{left:368px}.reviews .section-title::after{right:368px}
.review{position:absolute;top:146px;width:426px}
.review-1{left:148px}.review-2{left:625px}
.quote{position:relative;background:#ebebeb;height:112px;padding:14px 18px;font-size:12px;line-height:22px;color:#555}
.quote::after{content:"";position:absolute;left:40px;bottom:-14px;border:14px solid transparent;border-top-color:#ebebeb;border-bottom:0}
.stars{position:absolute;right:30px;bottom:12px;font-size:12px;color:var(--burgundy);letter-spacing:1px}
.stars i{color:#999;font-style:normal}
.reviewer{display:flex;align-items:center;gap:18px;margin:26px 0 0 36px}
.avatar{width:58px;height:58px;border-radius:50%;background:linear-gradient(135deg,#c99a7a,#7a5038)}
.reviewer b{display:block;font-size:15px;font-weight:600;color:#222}
.reviewer em{font-size:12px;color:#666}

/* footer */
.site-footer{height:326px;background:var(--footer);color:var(--white)}
.footer-brand{position:absolute;left:134px;top:66px;font-size:28px;font-weight:700;line-height:34px;width:220px}
.footer-info{position:absolute;left:126px;top:184px;font-size:13px;line-height:18px}
.footer-info div{display:flex;gap:12px;margin-bottom:18px}
.footer-col{position:absolute;top:50px;font-size:13px}
.col-links{left:416px}.col-heroes{left:634px}.col-contact{left:872px}
.footer-col h4{font-size:13px;font-weight:500;margin-bottom:26px}
.footer-col li{list-style:none;font-size:10px;font-weight:500;margin-bottom:17px;display:flex;gap:14px;align-items:center}
.col-heroes li{font-weight:700;font-size:10.5px}
.footer-col::before{content:"";position:absolute;left:-40px;top:0;width:1px;height:230px;background:rgba(255,255,255,.12)}
.field{width:204px;height:30px;border:1px solid rgba(255,255,255,.8);font-size:9px;padding:9px 8px;margin-bottom:16px}
.footer-submit{width:204px;height:30px;background:var(--burgundy);text-align:center;font-size:15px;font-weight:700;line-height:30px}
.footer-bar{height:60px;background:var(--footer-bar);color:#ccc;font-size:11px;text-align:center;line-height:60px}
</style>
</head>
<body>

<section class="hero">
  <div class="hero-photo" role="img" aria-label="Photo of a yellow house with a white picket fence among autumn trees"></div>
  <header class="topbar">
    <div class="brand">Dwellings &amp; Champions</div>
    <div class="account">
      <svg width="20" height="16" viewBox="0 0 20 16" fill="none" stroke="#8c1119" stroke-width="1.6"><path d="M8 2h9v12H8"/><path d="M1 8h10M8 5l3 3-3 3"/></svg>
      LOGIN &nbsp;/&nbsp; REGISTER
    </div>
    <div class="social"><span></span><span></span><span></span><span></span></div>
    <nav class="nav">
      <span>HOME</span><span>HOW IT WORKS</span><span>HERO ADVANTAGES</span><span>REALTORS</span><span>VENDORS</span><span>MEDIC PLEDGE PROGRAM</span><span>CONTACT US</span>
    </nav>
  </header>
  <h1 class="hero-title">Dwellings and Champions</h1>
  <p class="hero-sub">Get cash back with purchase of home</p>
  <div class="search-tabs"><span class="tab-buyer">Buyer</span><span class="tab-seller">Seller</span></div>
  <form class="search-panel">
    <div class="select">Hero Type...</div>
    <div class="select">Select interest...</div>
    <div class="select">City...</div>
    <div class="btn-submit">SUBMIT</div>
  </form>
</section>

<section class="savings">
  <h2 class="savings-head">HEROES WHO HAVE SAVED OVER</h2>
  <div class="savings-amount">$21,729,904.88</div>
  <div class="hero-grid">
    <div class="hero-type"><div class="icon" role="img" aria-label="Police officer icon"></div><div><h3>POLICE OFFICERS</h3><p>Our community police officers strive to work with residents to make our community ......</p><a>Read More</a></div></div>
    <div class="hero-type"><div class="icon" role="img" aria-label="First responder icon"></div><div><h3>FIRST RESPONDERS</h3><p>Our community police officers strive to work with residents to make our community ......</p><a>Read More</a></div></div>
    <div class="hero-type"><div class="icon" role="img" aria-label="Medical personnel icon"></div><div><h3>MEDICAL PERSONNEL</h3><p>Our community police officers strive to work with residents to make our community ......</p><a>Read More</a></div></div>
    <div class="hero-type"><div class="icon" role="img" aria-label="Educator icon"></div><div><h3>EDUCATORS</h3><p>Our community police officers strive to work with residents to make our community ......</p><a>Read More</a></div></div>
    <div class="hero-type"><div class="icon" role="img" aria-label="Military icon"></div><div><h3>MILITARY</h3><p>Our community police officers strive to work with residents to make our community ......</p><a>Read More</a></div></div>
    <div class="hero-type"><div class="icon" role="img" aria-label="Firefighter icon"></div><div><h3>FIREFIGHTERS</h3><p>Our community police officers strive to work with residents to make our community ......</p><a>Read More</a></div></div>
  </div>
</section>

<section class="how">
  <div class="video" role="img" aria-label="Video thumbnail: illustrated local hero greeting with a play button"></div>
  <h2>HOW IT WORKS</h2>
  <div class="how-body">
    <div class="how-text">
      <p>Lenders don't want borrowers receiving money upfront and so the Dwellings &amp; Champions program gives a cash rebate at the close of escrow. Since the Dwellings &amp; Champions program gives cash back at the close of escrow, it does not affect any other loan programs and/or discounts.</p>
      <p>On the purchase of a home, participating buying agents donate 25% of their commission to the Dwellings &amp; Champions non-profit program. D&amp;C then gives the hero a cash rebate upon close of escrow from</p>
    </div>
    <div class="btn-more">LEARN MORE</div>
  </div>
</section>

<section class="advantages">
  <h2 class="section-title">HERO ADVANTAGES</h2>
  <div class="adv-grid">
    <div class="adv"><div class="photo photo-officers" role="img" aria-label="Photo of two smiling police officers"></div><h3>HERO BUYERS</h3><p>HERO BUYERS GET <b>25%</b> REBATE AFTER ESCROW</p></div>
    <div class="adv"><div class="photo photo-family" role="img" aria-label="Photo of a family relaxing at home"></div><h3>HERO SELLERS</h3><p>HERO SELLERS GET <b>25%</b> OFF A NORMAL <b>6%</b> LISTING</p></div>
    <div class="adv"><div class="photo photo-medics" role="img" aria-label="Photo of medical staff attending a patient"></div><h3>PINECREST INSPECTIONS</h3><p>PINECREST INSPECTIONS WILL GIVE A 10% OFF DISCOUNT FOR HEROES</p></div>
  </div>
</section>

<section class="reviews">
  <h2 class="section-title">HERO REVIEWS</h2>
  <div class="review review-1">
    <div class="quote">I would like to take this opportunity to say that the quality of service offered by DC has been highly impressive.I would like to take this opportunity to<span class="stars">★★★<i>☆☆</i></span></div>
    <div class="reviewer"><div class="avatar" role="img" aria-label="Reviewer portrait"></div><div><b>Talia Brennick</b><em>Harbor Row LTD</em></div></div>
  </div>
  <div class="review review-2">
    <div class="quote">I would like to take this opportunity to say that the quality of service offered by DC has been highly impressive.I would like to take this opportunity to<span class="stars">★★★<i>☆☆</i></span></div>
    <div class="reviewer"><div class="avatar" role="img" aria-label="Reviewer portrait"></div><div><b>Talia Brennick</b><em>Harbor Row LTD</em></div></div>
  </div>
</section>

<footer class="site-footer">
  <div class="footer-brand">Dwellings &amp; Champions</div>
  <div class="footer-info">
    <div><svg width="12" height="16" viewBox="0 0 12 16"><path d="M6 0a6 6 0 0 0-6 6c0 4.5 6 10 6 10s6-5.5 6-10a6 6 0 0 0-6-6z" fill="#fff"/><circle cx="6" cy="6" r="2.2" fill="#0b1127"/></svg><span>It is a long established fact<br>that a reader will be<br>distracted by the</span></div>
    <div><svg width="14" height="14" viewBox="0 0 24 24"><path d="M6.6 10.8a15 15 0 0 0 6.6 6.6l2.2-2.2a1 1 0 0 1 1-.25 11.4 11.4 0 0 0 3.6.57 1 1 0 0 1 1 1V20a1 1 0 0 1-1 1A17 17 0 0 1 3 4a1 1 0 0 1 1-1h3.5a1 1 0 0 1 1 1c0 1.25.2 2.45.57 3.57a1 1 0 0 1-.25 1z" fill="#fff"/></svg><b>555-201- 0188</b></div>
  </div>
  <div class="footer-col col-links">
    <h4>Quick Links</h4>
    <ul>
      <li><span>→</span>HOME</li><li><span>→</span>HOW IT WORKS</li><li><span>→</span>HERO ADVANTAGES</li><li><span>→</span>REALTORS</li><li><span>→</span>VENDORS</li><li><span>→</span>MEDIC PLEDGE PROGRAM</li><li><span>→</span>CONTACT US</li>
    </ul>
  </div>
  <div class="footer-col col-heroes">
    <h4>Heroes</h4>
    <ul>
      <li><span>→</span>POLICE OFFICERS</li><li><span>→</span>FIRST RESPONDERS</li><li><span>→</span>MEDICAL PERSONNEL</li><li><span>→</span>EDUCATORS</li><li><span>→</span>MILITARY</li><li><span>→</span>FIREFIGHTERS</li>
    </ul>
  </div>
  <div class="footer-col col-contact">
    <h4>Contact Us</h4>
    <div class="field">Name...</div>
    <div class="field">Email...</div>
    <div class="field">Phone No...</div>
    <div class="footer-submit">SUBMIT</div>
  </div>
</footer>
<div class="footer-bar">dwellingsandchampions.example 2017. All rights reserved</div>

</body>
</html>
```